Vet Clinic Flyer

We will be distributing a flyer to surrounding suburbs to let them know who we are and where we are. We are a vet clinic tucked away in the suburbs, not particularly easy to find. We mostly service cats and dogs and like to promote ourselves as a vet that "loves your pets as much as you do". Attached is a business card we recently had designed, and our logo and letterhead. Would like the faded dog and cat involved like on the letter head, and all our contact details including email, website and pinwheelr plus a photo of our staff, and a map of where to find us. Flyer to be A5 sized, single sided. I have also attached some staff photos with pets that could be incorporated somehow too. Photo of outside clinic attached too but also inclusion is optional. A "like us on pinwheelr" would be good too.

Target Market(s)

anyone with a pet! dog lovers, cat lovers, families with pets, singles with pets.

Industry/Entity Type

Clinic

Font styles to use
Serif
Decorative
Other font styles liked:
• georgia

Colors
ec1f27
000000
ffffff

Requirements
Must have
• logo + all contact details including phone, address, email, pinwheelr and website. also must have map.
Nice to have
• "like us on pinwheelr" + staff photos + faded dog and cat that is featured on the letterhead. should focus on our colours red and black but with white so not too bold.
Should not have
• no times new roman or comic sans, I use "georgia" font for a lot of our stuff but doesnt have to be that. Not too busy and overloaded.

```html
<!DOCTYPE html>
<html lang="en">
<head>
<meta charset="utf-8">
<title>Harbour Paws Vet Care – Flyer</title>
<link rel="stylesheet" href="https://fonts.googleapis.com/css2?family=Montserrat:wght@800;900&family=Questrial&display=swap">
<style>
  :root {
    --red: #ec1f27;
    --red-glow: #f2564d;
    --black: #111111;
    --white: #ffffff;
    --grey-shade: #9a9a9a;
    --page: #e6e6e6;
  }
  * { box-sizing: border-box; margin: 0; padding: 0; }
  html, body { width: 1200px; height: 1000px; overflow: hidden; }
  body {
    background: var(--page);
    font-family: "Questrial", "Helvetica Neue", Arial, sans-serif;
    position: relative;
  }
  .flyer {
    position: absolute;
    left: 290px; top: 62px;
    width: 620px; height: 876px;
    background: var(--red);
    overflow: hidden;
    box-shadow: 0 10px 30px rgba(0,0,0,.25);
  }
  .hero-photo {
    position: absolute; left: 0; top: 0;
    width: 620px; height: 270px;
    background: linear-gradient(120deg, #7a1014 0%, #a8171d 45%, #8c1217 100%);
  }
  .headline-tab {
    position: absolute; left: 110px; top: 200px;
    width: 420px; height: 330px;
    border-radius: 210px 210px 0 0;
    background: radial-gradient(ellipse at 50% 35%, var(--red-glow) 0%, var(--red) 70%);
  }
  .faded-pets {
    position: absolute; left: 170px; top: 300px;
    width: 360px; height: 360px;
    border-radius: 50%;
    background: radial-gradient(circle, rgba(150,10,15,.18) 0%, rgba(150,10,15,0) 70%);
  }
  .headline {
    position: absolute; left: 110px; top: 222px; width: 420px;
    text-align: center;
    font-family: "Montserrat", Arial, sans-serif;
    font-weight: 900;
    color: var(--white);
    line-height: .9;
    text-transform: uppercase;
    text-shadow: 2px 2px 0 var(--grey-shade), 4px 4px 0 #7d7d7d;
  }
  .headline .small { display: block; font-size: 40px; letter-spacing: -1px; }
  .headline .big { display: block; font-size: 112px; letter-spacing: -3px; margin: 2px 0; }
  .staff-photos {
    position: absolute; left: 150px; top: 462px;
    display: flex; gap: 20px;
  }
  .staff-photo {
    width: 92px; height: 92px;
    border: 6px solid var(--white);
    background: linear-gradient(160deg, #5a5a5a, #2a2a2a);
    box-shadow: 0 3px 6px rgba(0,0,0,.35);
  }
  .brand-box {
    position: absolute; left: 456px; top: 636px;
    width: 144px; height: 146px;
    background: var(--white);
    border: 4px solid var(--white);
    outline: 2px solid var(--black);
    display: flex; flex-direction: column; justify-content: center; align-items: center;
    text-align: center;
    color: var(--black);
    font-size: 20px; line-height: 1.15;
  }
  .social {
    position: absolute; left: 26px; top: 650px;
    color: var(--white);
    font-family: "Montserrat", Arial, sans-serif;
    font-weight: 800; line-height: 1.05;
  }
  .social .lead { display: block; font-size: 13px; }
  .social .network { display: block; font-size: 22px; }
  .contacts {
    position: absolute; left: 26px; top: 706px;
    color: var(--white); font-size: 20px;
    list-style: none;
  }
  .contacts li { display: flex; align-items: center; gap: 12px; height: 30px; }
  .contacts svg { width: 20px; height: 20px; flex: none; }
  .contacts .fax-icon { margin-left: 30px; }
  .web-band {
    position: absolute; left: 0; bottom: 0;
    width: 620px; height: 70px;
    background: var(--black);
    color: var(--white);
    font-size: 28px;
    display: flex; align-items: center; justify-content: center;
    letter-spacing: .5px;
  }
</style>
</head>
<body>
  <main class="flyer">
    <div class="hero-photo" role="img" aria-label="Staff member cuddling a cat inside the clinic, red duotone photo"></div>
    <div class="headline-tab"></div>
    <div class="faded-pets" role="img" aria-label="Faded line drawing of a cat and dog"></div>

    <h1 class="headline">
      <span class="small">Loves your</span>
      <span class="big">Pets</span>
      <span class="small">As much</span>
      <span class="small">As you do</span>
    </h1>

    <div class="staff-photos">
      <div class="staff-photo" role="img" aria-label="Staff member holding a dog"></div>
      <div class="staff-photo" role="img" aria-label="Staff member holding a small dog"></div>
      <div class="staff-photo" role="img" aria-label="Staff member holding a black dog"></div>
    </div>

    <div class="brand-box">
      <span>harbour paws<br>vet care</span>
    </div>

    <p class="social"><span class="lead">Like us on</span><span class="network">pinwheelr</span></p>

    <ul class="contacts">
      <li>
        <svg viewBox="0 0 20 20"><path d="M10 1a6.5 6.5 0 0 0-6.5 6.5C3.5 12 10 19 10 19s6.5-7 6.5-11.5A6.5 6.5 0 0 0 10 1zm0 9a2.5 2.5 0 1 1 0-5 2.5 2.5 0 0 1 0 5z" fill="#fff"/></svg>
        Shop 4/9 Keel Place Marlow NT 0820
      </li>
      <li>
        <svg viewBox="0 0 20 20"><circle cx="10" cy="10" r="8.5" fill="none" stroke="#fff" stroke-width="1.6"/><path d="M7 5.5l1.6 2.2-1 1.2c.6 1.3 1.6 2.3 2.8 2.9l1.2-1 2.2 1.6-.9 1.8c-3.4-.4-6.3-3.3-6.7-6.7z" fill="#fff"/></svg>
        08 8100 2461
        <svg class="fax-icon" viewBox="0 0 20 20"><rect x="2" y="7" width="16" height="9" rx="1.5" fill="#fff"/><rect x="5" y="3" width="10" height="5" fill="#fff"/><rect x="6" y="10" width="8" height="1.5" fill="#ec1f27"/><rect x="6" y="13" width="8" height="1.5" fill="#ec1f27"/></svg>
        08 8100 2479
      </li>
      <li>
        <svg viewBox="0 0 20 20"><rect x="1.5" y="4" width="17" height="12" fill="none" stroke="#fff" stroke-width="1.6"/><path d="M1.5 4l8.5 7 8.5-7" fill="none" stroke="#fff" stroke-width="1.6"/></svg>
        hello@harbourpawsvets.net
      </li>
    </ul>

    <footer class="web-band">www.harbourpawsvetcare.com.au</footer>
  </main>
</body>
</html>
```